PebbleLoom screens tidy up

We would like advice on how to better present the following home page and overview pages.

The existing website is functional, but the pages don't appear professionals and pleasing to the eye. We would specifically like feedback on alignment and padding of icons and text to make the screen more appealing and polished.

We are following the willow design system.

1 page

Sans Serif
• IBM Plex, Poppins

```html
<!DOCTYPE html>
<html lang="en">
<head>
<meta charset="utf-8">
<title>PebbleLoom – Overview and Home screens</title>
<link href="https://fonts.googleapis.com/css2?family=Montserrat:wght@400;500;600;700&display=swap" rel="stylesheet">
<style>
  :root{
    --navy:#243259;
    --orange:#f0821f;
    --orange-soft:#fdf1e6;
    --ice:#e4edf5;
    --ink:#1d1d1f;
    --line:#e2e4ea;
    --page:#ffffff;
  }
  *{box-sizing:border-box;margin:0;padding:0}
  html,body{width:797px;height:1200px;overflow:hidden;background:var(--page);font-family:"Montserrat",sans-serif;color:var(--ink)}
  .screen{position:absolute;left:43px;width:711px;height:528px;background:#fff;box-shadow:0 8px 18px rgba(0,0,0,.18);overflow:hidden}
  .screen--overview{top:49px}
  .screen--home{top:623px}
  .abs{position:absolute;white-space:nowrap}

  /* sidebar */
  .sidebar{position:absolute;left:0;top:0;width:130px;height:100%;background:var(--navy)}
  .brand{position:absolute;left:6px;top:13px;display:flex;align-items:center;gap:6px}
  .brand-dot{width:24px;height:24px;border-radius:50%;background:var(--orange)}
  .brand-name{color:#fff;font-weight:600;font-size:15px;letter-spacing:-.4px}
  .nav-item{position:absolute;left:0;width:130px;height:16px;display:flex;align-items:center;color:#fff;font-size:7.5px;font-weight:600}
  .nav-item svg{position:absolute;left:8px;width:9px;height:9px}
  .nav-item span{position:absolute;left:33px}
  .nav-plus{position:absolute;right:10px!important;left:auto!important;font-size:10px;font-weight:500}
  .nav-group{position:absolute;left:0;width:130px;height:23px;background:var(--ice)}
  .nav-group .tab{position:absolute;left:22px;right:0;top:0;bottom:0;background:var(--orange);clip-path:polygon(6px 0,100% 0,100% 100%,6px 100%,0 50%)}
  .nav-group svg{position:absolute;left:7px;top:7px;width:9px;height:9px}
  .nav-group span{position:absolute;left:33px;top:0;line-height:23px;color:#fff;font-size:7.5px;font-weight:600}
  .nav-group .chev{left:auto;right:8px;font-size:7px}
  .nav-sub{position:absolute;left:49px;color:#fff;font-size:7.5px;font-weight:600;line-height:16px}
  .nav-sub--active{position:absolute;left:34px;width:96px;height:23px;background:var(--ice);clip-path:polygon(0 0,100% 0,100% 100%,0 100%,5px 50%)}
  .nav-sub--active span{position:absolute;left:15px;line-height:23px;color:var(--orange);font-size:7.5px;font-weight:600}

  /* header */
  .eyebrow{font-size:8px;font-weight:700}
  .page-title{font-size:17px;font-weight:600;color:var(--orange)}
  .avatar{position:absolute;left:593px;width:26px;height:26px;border-radius:50%;background:linear-gradient(135deg,#d9cbbd,#8a7767);border:1px solid #f3c79c}
  .welcome{font-size:8.5px;font-weight:500;left:626px}

  .section-title{font-size:10px;font-weight:500}
  .card{position:absolute;background:#fff;border:1px solid var(--line);border-radius:3px;box-shadow:0 1px 3px rgba(0,0,0,.06)}
  .card-title{font-size:9px;font-weight:700;color:var(--orange)}
  .card-text{font-size:7.5px;font-weight:500}
  .big-num{font-size:27px;font-weight:700;line-height:1}
  .btn{position:absolute;background:var(--orange);color:#fff;font-size:7.5px;font-weight:500;display:flex;align-items:center}
  .icon{position:absolute}
  .divider{position:absolute;height:1px;background:var(--line)}
  .center{text-align:center;white-space:normal}
  .tiny{font-size:5px;font-weight:500}
  .halo{position:absolute;width:68px;height:68px;border-radius:50%;background:var(--orange-soft)}
</style>
</head>
<body>

<!-- Campaign overview screen -->
<section class="screen screen--overview">
  <nav class="sidebar">
    <div class="brand"><div class="brand-dot"></div><span class="brand-name">PebbleLoom</span></div>
    <div class="nav-item" style="top:68px"><svg viewBox="0 0 10 10"><circle cx="5" cy="5" r="4" fill="#8d98b3"/></svg><span>Home</span></div>
    <div class="nav-item" style="top:96px"><svg viewBox="0 0 10 10" fill="#8d98b3"><rect x="1" y="1" width="8" height="2"/><rect x="1" y="4" width="8" height="2"/><rect x="1" y="7" width="8" height="2"/></svg><span>All alerts</span></div>
    <div class="nav-item" style="top:124px"><svg viewBox="0 0 10 10" fill="#8d98b3"><circle cx="4" cy="3" r="2.2"/><rect x="1" y="6" width="7" height="3" rx="1.5"/></svg><span>Manage</span></div>
    <div class="nav-item" style="top:150px"><svg viewBox="0 0 10 10" fill="#8d98b3"><path d="M1 4h3l4-3v8L4 6H1z"/></svg><span>Campaigns</span><span class="nav-plus">+</span></div>
    <div class="nav-group" style="top:177px"><svg viewBox="0 0 10 10" fill="#8d98b3"><path d="M1 4h3l4-3v8L4 6H1z"/></svg><div class="tab"></div><span>My Custom Campaign</span><span class="chev">⌃</span></div>
    <div class="nav-sub--active" style="top:210px"><span>Overview</span></div>
    <div class="nav-sub" style="top:240px">Files &amp; HoneyTokens</div>
    <div class="nav-sub" style="top:270px">Resources</div>
    <div class="nav-sub" style="top:299px">Alerts</div>
    <div class="nav-sub" style="top:330px">Settings</div>
    <div class="nav-group" style="top:355px"><svg viewBox="0 0 10 10" fill="#8d98b3"><rect x="2" y="1" width="6" height="8" rx="1"/></svg><div class="tab"></div><span>Default Campaign</span><span class="chev">⌄</span></div>
  </nav>

  <div class="abs eyebrow" style="left:137px;top:15px">MY CUSTOM CAMPAIGN</div>
  <div class="abs page-title" style="left:137px;top:22px">Overview</div>
  <div class="avatar" role="img" aria-label="User profile photo" style="top:18px"></div>
  <div class="abs welcome" style="top:26px">Welcome, Owen</div>

  <div class="abs section-title" style="left:138px;top:58px">Campaign</div>
  <div class="card" style="left:137px;top:75px;width:560px;height:52px">
    <svg class="icon" style="left:12px;top:12px" width="28" height="28" viewBox="0 0 28 28"><circle cx="14" cy="14" r="13.5" fill="#fff" stroke="#e2e4ea"/><path d="M8 12h4l6-4v12l-6-4H8z" fill="none" stroke="#333" stroke-width="1"/><circle cx="12" cy="9" r="1.6" fill="none" stroke="var(--orange)"/></svg>
    <div class="abs card-title" style="left:52px;top:13px">My Custom Campaign</div>
    <div class="abs card-text" style="left:52px;top:27px">This is my custom campaign for finding i</div>
    <div class="btn" style="left:502px;top:14px;width:46px;height:23px;justify-content:center">Custom</div>
  </div>

  <div class="abs section-title" style="left:138px;top:150px">Campaign Organisation</div>
  <div class="card" style="left:137px;top:168px;width:560px;height:86px">
    <svg class="icon" style="left:15px;top:7px" width="26" height="28" viewBox="0 0 26 28" fill="none" stroke="#222" stroke-width="1"><rect x="2" y="8" width="9" height="19"/><rect x="11" y="2" width="13" height="25"/><path d="M5 12h3M5 16h3M5 20h3M14 6h2M19 6h2M14 10h2M19 10h2M14 14h2M19 14h2"/><path d="M15 27v-6h5v6" stroke="var(--orange)"/></svg>
    <div class="abs card-title" style="left:52px;top:12px">Self-enabling Deliverables Proprietary Limited</div>
    <div class="abs card-text" style="left:52px;top:27px">Standard</div>
    <svg class="icon" style="left:16px;top:47px" width="24" height="22" viewBox="0 0 24 22" fill="none" stroke="var(--orange)" stroke-width="1"><circle cx="12" cy="4" r="2.5"/><circle cx="5" cy="9" r="2"/><circle cx="19" cy="9" r="2"/><path d="M1 21v-5a4 4 0 0 1 8 0M15 16a4 4 0 0 1 8 0v5M6 21v-7a6 6 0 0 1 12 0v7z"/></svg>
    <div class="abs big-num" style="left:52px;top:46px">86</div>
    <div class="abs card-title" style="left:337px;top:12px">Unleash bleeding-edge mindshare</div>
    <div class="abs card-text" style="left:337px;top:27px">8 hours age</div>
    <svg class="icon" style="left:304px;top:45px" width="26" height="26" viewBox="0 0 26 26" fill="none" stroke-width="1"><circle cx="13" cy="13" r="4" stroke="#222"/><g stroke="#222"><circle cx="13" cy="3" r="1.6"/><circle cx="13" cy="23" r="1.6"/><circle cx="3" cy="13" r="1.6"/><circle cx="23" cy="13" r="1.6"/></g><g stroke="var(--orange)"><circle cx="6" cy="6" r="1.6"/><circle cx="20" cy="6" r="1.6"/><circle cx="6" cy="20" r="1.6"/><circle cx="20" cy="20" r="1.6"/></g></svg>
    <div class="abs big-num" style="left:337px;top:46px">8</div>
  </div>

  <div class="abs section-title" style="left:138px;top:286px">Files &amp; Honey Tokens</div>
  <div class="abs section-title" style="left:428px;top:286px">Resources</div>
  <div class="card" style="left:137px;top:302px;width:280px;height:86px">
    <svg class="icon" style="left:15px;top:8px" width="24" height="26" viewBox="0 0 24 26" fill="none" stroke-width="1"><path d="M2 25h21M3 25v-6h4v6M10 25v-10h4v10M17 25V9h4v16" stroke="#222"/><path d="M2 14l6-5 4 3 9-9M17 3h4v4" stroke="var(--orange)"/></svg>
    <div class="abs card-title" style="left:52px;top:14px">Statistics</div>
    <svg class="icon" style="left:27px;top:52px" width="14" height="14" viewBox="0 0 14 14"><circle cx="7" cy="7" r="7" fill="var(--orange)"/><path d="M4 7l2 2 4-4" fill="none" stroke="#fff" stroke-width="1.5"/></svg>
    <div class="abs big-num" style="left:52px;top:46px">0</div>
    <svg class="icon" style="left:115px;top:46px" width="25" height="25" viewBox="0 0 26 26" fill="none" stroke-width="1"><circle cx="13" cy="13" r="4" stroke="#222"/><g stroke="#222"><circle cx="13" cy="3" r="1.6"/><circle cx="13" cy="23" r="1.6"/><circle cx="3" cy="13" r="1.6"/><circle cx="23" cy="13" r="1.6"/></g><g stroke="var(--orange)"><circle cx="6" cy="6" r="1.6"/><circle cx="20" cy="6" r="1.6"/><circle cx="6" cy="20" r="1.6"/><circle cx="20" cy="20" r="1.6"/></g></svg>
    <div class="abs big-num" style="left:146px;top:46px">30</div>
  </div>
  <div class="card" style="left:428px;top:302px;width:269px;height:86px">
    <svg class="icon" style="left:9px;top:10px" width="30" height="28" viewBox="0 0 30 28" fill="none" stroke-width="1"><circle cx="15" cy="14" r="4" stroke="#222"/><circle cx="15" cy="14" r="1.5" stroke="#222"/><path d="M7 8a10 10 0 0 1 16 0M7 22a10 10 0 0 0 16 0" stroke="#222"/><g stroke="var(--orange)"><circle cx="15" cy="3" r="2"/><circle cx="4" cy="15" r="2"/><circle cx="26" cy="15" r="2"/><path d="M1 22a3 3 0 0 1 6 0M23 22a3 3 0 0 1 6 0"/></g></svg>
    <div class="abs card-text" style="left:48px;top:14px;line-height:10.5px">Generate a collection of fictional organisations,<br>Custom templates, Uploaded &nbsp;files and logos.</div>
  </div>

  <div class="abs section-title" style="left:138px;top:412px">Alerts</div>
  <div class="card" style="left:137px;top:429px;width:560px;height:85px">
    <svg class="icon" style="left:14px;top:8px" width="24" height="22" viewBox="0 0 24 22" fill="none" stroke-width="1"><path d="M12 1L23 21H1z" stroke="#222"/><path d="M12 8v7M12 17v1.5" stroke="var(--orange)" stroke-width="1.4"/></svg>
    <div class="abs card-title" style="left:52px;top:12px">Alert Statistics will appear here</div>
  </div>
</section>

<!-- Home screen -->
<section class="screen screen--home">
  <nav class="sidebar">
    <div class="brand"><div class="brand-dot"></div><span class="brand-name">PebbleLoom</span></div>
    <div class="nav-item" style="top:68px"><svg viewBox="0 0 10 10"><circle cx="5" cy="5" r="4" fill="#8d98b3"/></svg><span>Home</span></div>
    <div class="nav-item" style="top:96px"><svg viewBox="0 0 10 10" fill="#8d98b3"><rect x="1" y="1" width="8" height="2"/><rect x="1" y="4" width="8" height="2"/><rect x="1" y="7" width="8" height="2"/></svg><span>All alerts</span></div>
    <div class="nav-item" style="top:124px"><svg viewBox="0 0 10 10" fill="#8d98b3"><circle cx="4" cy="3" r="2.2"/><rect x="1" y="6" width="7" height="3" rx="1.5"/></svg><span>Manage</span></div>
    <div class="nav-item" style="top:150px"><svg viewBox="0 0 10 10" fill="#8d98b3"><path d="M1 4h3l4-3v8L4 6H1z"/></svg><span>Campaigns</span><span class="nav-plus">+</span></div>
    <div class="nav-group" style="top:177px"><svg viewBox="0 0 10 10" fill="#8d98b3"><path d="M1 4h3l4-3v8L4 6H1z"/></svg><div class="tab"></div><span>My Custom Campaign</span><span class="chev">⌃</span></div>
    <div class="nav-sub" style="top:210px">Overview</div>
    <div class="nav-sub" style="top:240px">Files &amp; HoneyTokens</div>
    <div class="nav-sub" style="top:270px">Resources</div>
    <div class="nav-sub" style="top:299px">Alerts</div>
    <div class="nav-sub" style="top:330px">Settings</div>
    <div class="nav-group" style="top:355px"><svg viewBox="0 0 10 10" fill="#8d98b3"><rect x="2" y="1" width="6" height="8" rx="1"/></svg><div class="tab"></div><span>Default Campaign</span><span class="chev">⌄</span></div>
  </nav>

  <div class="abs page-title" style="left:137px;top:15px">Home</div>
  <div class="avatar" role="img" aria-label="User profile photo" style="top:18px"></div>
  <div class="abs welcome" style="top:26px">Welcome, Owen</div>

  <div class="abs section-title" style="left:138px;top:58px">Teamspace</div>
  <div class="card" style="left:137px;top:76px;width:560px;height:52px">
    <div class="abs card-title" style="left:16px;top:12px">Default</div>
    <div class="abs card-text" style="left:16px;top:26px">The default client is created as a part of your user account.</div>
  </div>

  <div class="abs section-title" style="left:138px;top:150px">Subscription overview</div>
  <div class="abs section-title" style="left:313px;top:150px">Files &amp; HoneyTokens</div>
  <div class="card" style="left:137px;top:168px;width:164px;height:81px">
    <svg class="icon" style="left:69px;top:7px" width="26" height="26" viewBox="0 0 26 26" fill="none" stroke-width="1"><path d="M3 25v-5h3v5zM9 25v-9h3v9zM15 25v-7h3v7zM21 25V9h3v16z" stroke="#222"/><path d="M3 14l6-5 6 3 8-9" stroke="var(--orange)"/></svg>
    <div class="abs card-title center" style="left:0;width:164px;top:39px">Starter pack usage</div>
    <div class="divider" style="left:7px;width:150px;top:54px"></div>
    <div class="abs card-text center" style="left:0;width:164px;top:63px">0 files active out of 10 allowed</div>
  </div>
  <div class="card" style="left:312px;top:168px;width:164px;height:81px">
    <svg class="icon" style="left:67px;top:6px" width="28" height="28" viewBox="0 0 28 28" fill="none" stroke-width="1"><path d="M2 26h24M3 26v-9h4v9zM9 26v-6h4v6zM15 26v-11h4v11zM21 26V12h4v14z" stroke="#222"/><path d="M3 9l5-3 5 4 5-5 6 4" stroke="var(--orange)"/></svg>
    <div class="abs card-title center" style="left:0;width:164px;top:40px">Statistics</div>
    <div class="divider" style="left:15px;width:134px;top:54px"></div>
    <div class="abs" style="left:42px;top:58px;font-size:14px;font-weight:700">0</div>
    <div class="abs" style="left:106px;top:58px;font-size:14px;font-weight:700">30</div>
  </div>

  <div class="abs section-title" style="left:138px;top:289px">Campaigns</div>
  <div class="btn" style="left:202px;top:285px;width:86px;height:22px;padding:0 6px;justify-content:space-between"><span>New Campaign</span><span>+</span></div>

  <div class="card" style="left:137px;top:321px;width:164px;height:168px">
    <div class="abs card-title center" style="left:0;width:164px;top:8px">My custom campaign</div>
    <div class="abs card-text center" style="left:0;width:164px;top:21px">This is my custom campaign for finding I</div>
    <div class="halo" style="left:48px;top:51px"></div>
    <svg class="icon" style="left:64px;top:67px" width="36" height="36" viewBox="0 0 36 36" fill="none" stroke-width="1.4"><path d="M16 4a14 14 0 1 0 14 14H16z" stroke="#222"/><path d="M20 1a14 14 0 0 1 14 14H20z" stroke="var(--orange)"/><path d="M20 19h13l-7 9z" stroke="#222"/></svg>
    <div class="abs" style="left:30px;top:124px;font-size:19px;font-weight:500;color:var(--orange);line-height:1">0</div>
    <div class="abs tiny" style="left:48px;top:127px">Active</div>
    <div class="abs card-text" style="left:48px;top:135px">Files and HoneyTokens</div>
    <div class="abs tiny center" style="left:0;width:164px;top:153px">Active since: Jul 25 2023 13:12</div>
  </div>
  <div class="card" style="left:312px;top:321px;width:164px;height:168px">
    <div class="abs card-title center" style="left:0;width:164px;top:8px">Dafault Campaign</div>
    <div class="abs card-text center" style="left:20px;width:124px;top:21px;line-height:12px">Define your own mission, or combine differen..</div>
    <div class="halo" style="left:48px;top:51px"></div>
    <svg class="icon" style="left:66px;top:70px" width="30" height="30" viewBox="0 0 30 30" fill="none" stroke-width="1.4"><path d="M3 2v25h25" stroke="#222"/><path d="M8 21l6-7 4 4 7-8" stroke="var(--orange)"/></svg>
    <div class="abs" style="left:30px;top:124px;font-size:19px;font-weight:500;color:var(--orange);line-height:1">0</div>
    <div class="abs tiny" style="left:48px;top:127px">Active</div>
    <div class="abs card-text" style="left:48px;top:135px">Files and HoneyTokens</div>
    <div class="abs tiny center" style="left:0;width:164px;top:153px">Active since: Jul 20 2023 12:17</div>
  </div>
</section>

</body>
</html>
```